TRU PEAK POWER.

I'd like my business logo.
contact name: Desmond Halvik
phone:0438275160
email: info@trupeakpower.net.au
website: www.trupeakpower.net.au

services:
solar
battery storage
LED lighting
energy saving solutions
general electrical
I'd like the design to look professional

Target Market(s)

Everyone

Industry/Entity Type

Business

Contact Information for Business Card

as described above

Requirements
Must have
• Id like the colours and the design to work well with my logo.

```html
<!DOCTYPE html>
<html lang="en">
<head>
<meta charset="utf-8">
<title>Tru Peak Power – Business Card</title>
<link rel="stylesheet" href="https://fonts.googleapis.com/css2?family=Lato:wght@300;400;700&display=swap">
<style>
  :root {
    --backdrop: #1d1f1d;
    --card-white: #f6f6f4;
    --green-deep: #1f5e1c;
    --green-mid: #3f8f25;
    --green-bright: #7dbb2c;
    --green-lime: #a6cf3a;
    --sun-orange: #e8a21c;
    --ink: #3a3a3a;
    --ink-soft: #6b6b6b;
  }
  * { box-sizing: border-box; margin: 0; padding: 0; }
  html, body { width: 1200px; height: 900px; overflow: hidden; }
  body {
    background: var(--backdrop);
    font-family: "Lato", Arial, sans-serif;
    display: flex;
    flex-direction: column;
    align-items: center;
    justify-content: center;
    gap: 40px;
  }
  .card {
    position: relative;
    width: 660px;
    height: 380px;
    border-radius: 18px;
    overflow: hidden;
    background: var(--card-white);
  }

  /* Front */
  .stripe-field {
    position: absolute;
    left: 0; right: 0;
    background: linear-gradient(90deg,
      var(--green-deep) 0%, var(--green-mid) 18%, var(--green-bright) 30%,
      var(--green-deep) 45%, var(--green-lime) 58%, var(--green-mid) 72%,
      var(--green-deep) 86%, var(--green-bright) 100%);
  }
  .stripe-field.top { top: 0; height: 40px; }
  .stripe-field.bottom { top: 205px; bottom: 0; }
  .logo-band {
    position: absolute;
    top: 40px; left: 0; right: 0;
    height: 165px;
    display: flex;
    align-items: center;
    justify-content: flex-end;
    padding-right: 56px;
    gap: 16px;
  }
  .logo-mark {
    width: 46px; height: 46px;
    border-radius: 50%;
    background: var(--green-bright);
  }
  .logo-name {
    font-weight: 700;
    font-size: 52px;
    color: var(--green-mid);
    letter-spacing: 1px;
  }
  .service-strip {
    position: absolute;
    top: 250px; left: 0; right: 0;
    height: 34px;
    background: var(--card-white);
    display: flex;
    align-items: center;
    justify-content: space-evenly;
    font-size: 18px;
    color: var(--green-deep);
  }
  .service-strip span::before {
    content: "";
    display: inline-block;
    width: 11px; height: 11px;
    background: var(--green-deep);
    margin-right: 6px;
    vertical-align: 0;
  }

  /* Back */
  .back { padding: 34px 40px; color: var(--ink); }
  .contact-line {
    display: flex;
    align-items: center;
    gap: 10px;
    font-size: 19px;
    font-weight: 300;
    position: absolute;
  }
  .icon {
    width: 24px; height: 24px;
    border-radius: 5px;
    background: var(--green-bright);
    display: flex; align-items: center; justify-content: center;
  }
  .phone { top: 48px; left: 40px; }
  .email { top: 150px; left: 150px; }
  .web { top: 232px; right: 40px; }
  .person {
    position: absolute;
    top: 78px; left: 250px;
  }
  .person-name {
    font-size: 42px;
    font-weight: 300;
    letter-spacing: 2px;
    text-transform: uppercase;
    color: var(--ink);
  }
  .person-name .surname { color: var(--green-bright); }
  .person-title {
    font-size: 17px;
    font-weight: 300;
    letter-spacing: 3px;
    color: var(--ink-soft);
    text-transform: uppercase;
  }
  .company {
    position: absolute;
    top: 226px; left: 40px;
  }
  .company-name {
    font-size: 19px;
    font-weight: 700;
    color: var(--green-mid);
    letter-spacing: 1px;
  }
  .company-address {
    font-size: 17px;
    font-weight: 300;
    text-transform: uppercase;
    letter-spacing: 1px;
    color: var(--ink);
    margin-top: 4px;
  }
  .edge-rule {
    position: absolute;
    left: 0; right: 0; bottom: 36px;
    height: 10px;
    border-top: 2px dotted #9a9a9a;
    border-bottom: 2px solid var(--green-deep);
  }
</style>
</head>
<body>

<section class="card front">
  <div class="stripe-field top" role="img" aria-label="Green striped texture band"></div>
  <div class="logo-band">
    <div class="logo-mark"></div>
    <div class="logo-name">TRU PEAK POWER</div>
  </div>
  <div class="stripe-field bottom" role="img" aria-label="Green striped texture band"></div>
  <div class="service-strip">
    <span>LED Lighting</span>
    <span>Battery Storage</span>
    <span>Solar</span>
    <span>Energy Saving Solutions</span>
  </div>
</section>

<section class="card back">
  <div class="contact-line phone">
    <span class="icon">
      <svg width="14" height="14" viewBox="0 0 14 14"><rect x="3" y="1" width="8" height="12" rx="1.5" fill="none" stroke="#fff" stroke-width="1.6"/></svg>
    </span>
    0438 275 160
  </div>

  <div class="person">
    <div class="person-name">Desmond <span class="surname">Halvik</span></div>
    <div class="person-title">Managing Director</div>
  </div>

  <div class="contact-line email">
    <span class="icon">
      <svg width="14" height="14" viewBox="0 0 14 14"><text x="7" y="11" font-size="12" text-anchor="middle" fill="#fff" font-family="Arial, sans-serif">@</text></svg>
    </span>
    info@trupeakpower.net.au
  </div>

  <div class="company">
    <div class="company-name">TRU PEAK POWER SOLUTIONS</div>
    <div class="company-address">214 Carrow Lane, Elmbrook VIC 3390</div>
  </div>

  <div class="contact-line web">
    <span class="icon">
      <svg width="16" height="16" viewBox="0 0 16 16"><circle cx="8" cy="8" r="6" fill="none" stroke="#fff" stroke-width="1.4"/><path d="M2 8h12M8 2c-3 3-3 9 0 12M8 2c3 3 3 9 0 12" fill="none" stroke="#fff" stroke-width="1.1"/></svg>
    </span>
    www.trupeakpower.net.au
  </div>

  <div class="edge-rule"></div>
</section>

</body>
</html>
```